Innovative Consulting Firm Needs New Business Cards and Stationary

Our Innovative Consulting Firm, Larkfield Consulting, is in need of new business cards and stationary designs. We want two-sided cards that incorporate our logo, which is attached. We are looking for something not too formal, but is professional and slick.

Card should have the following information:
Name (ex. Tom Bradley)
Title (ex. Manager)
Address (ex. 24680 Cedar Lane)
Address 2 (ex. Suite 100)
City
State
Zip Code
Mobile
Email

The card should also have our website: www.larkfieldconsulting.example

Industry/Entity Type

Management Consulting

Contact Information for Business Card

Name (ex. Tom Bradley)
Title (ex. Manager)
Address 2 (ex. Suite 100)
City
State
Zip Code
Mobile
Email

Font styles to use
Sans Serif

Requirements
Must have
• The colors on the card must match the colors in the logo. The exact color codes are attached in a pdf.
Nice to have
• The Company's Tagline is "Focused on your Future". This might be nice to incorporate, but not necessary.

```html
<!DOCTYPE html>
<html lang="en">
<head>
<meta charset="utf-8">
<title>Larkfield Consulting – Business Card</title>
<link href="https://fonts.googleapis.com/css2?family=Arimo:wght@400;700&family=Orbitron:wght@700&display=swap" rel="stylesheet">
<style>
  :root {
    --navy: #1f4f7a;
    --gold: #f5ae1c;
    --white: #ffffff;
    --stage: #000000;
  }
  * { margin: 0; padding: 0; box-sizing: border-box; }
  html, body { width: 999px; height: 1200px; overflow: hidden; background: var(--stage); }
  body { position: relative; font-family: "Arimo", Arial, sans-serif; }

  .card { position: absolute; width: 876px; height: 500px; overflow: hidden; }
  .card--front { left: 42px; top: 84px; background: var(--white); }
  .card--back { left: 41px; top: 609px; background: var(--navy); }

  .card__wave { position: absolute; left: 0; top: 0; width: 876px; height: 500px; }

  .brand { position: absolute; text-align: right; }
  .brand__name { display: block; font-weight: 400; line-height: 1; letter-spacing: 1px; }
  .brand__tag { display: block; font-size: 17px; letter-spacing: 6px; margin-top: 4px; }

  .card--front .brand { left: 210px; top: 76px; width: 458px; color: var(--navy); }
  .card--front .brand__name { font-size: 74px; }
  .card--back .brand { left: 188px; top: 196px; width: 502px; color: var(--white); }
  .card--back .brand__name { font-size: 80px; }
  .card--back .brand__tag { font-size: 18px; letter-spacing: 7px; margin-top: 6px; }

  .holder { position: absolute; left: 58px; top: 328px; color: var(--white); }
  .holder__name { font-family: "Orbitron", "Arimo", sans-serif; font-weight: 700; font-size: 29px; color: var(--gold); letter-spacing: 1px; }
  .holder__title { font-size: 21px; margin: 8px 0 0 5px; }
  .holder__address { font-size: 20px; line-height: 30px; margin: 14px 0 0 4px; }

  .contacts { position: absolute; left: 474px; top: 328px; list-style: none; color: var(--white); font-size: 21px; }
  .contacts__item { display: flex; align-items: center; height: 35px; }
  .contacts__icon { width: 22px; height: 22px; margin-right: 19px; fill: var(--white); }
</style>
</head>
<body>

<section class="card card--front">
  <svg class="card__wave" viewBox="0 0 876 500" aria-hidden="true">
    <path fill="var(--navy)" d="M0,228 C120,290 300,340 478,291 C560,262 660,200 760,208 C820,212 850,225 876,239 L876,500 L0,500 Z"/>
    <path fill="var(--gold)" d="M0,178 C110,258 300,306 483,281 C300,318 110,292 0,212 Z"/>
  </svg>

  <div class="brand">
    <span class="brand__name">Larkfield</span>
    <span class="brand__tag">CONSULTING</span>
  </div>

  <div class="holder">
    <h1 class="holder__name">Tom Bradley</h1>
    <p class="holder__title">Manager</p>
    <p class="holder__address">24680 Cedar Lane)<br>suit # 00, Lorem ipsum</p>
  </div>

  <ul class="contacts">
    <li class="contacts__item">
      <svg class="contacts__icon" viewBox="0 0 24 24"><path d="M6.6 10.8a15 15 0 0 0 6.6 6.6l2.2-2.2a1 1 0 0 1 1-.25 11.4 11.4 0 0 0 3.6.6 1 1 0 0 1 1 1V20a1 1 0 0 1-1 1A17 17 0 0 1 3 4a1 1 0 0 1 1-1h3.5a1 1 0 0 1 1 1c0 1.25.2 2.45.6 3.6a1 1 0 0 1-.25 1z"/></svg>
      00 0000 0000
    </li>
    <li class="contacts__item">
      <svg class="contacts__icon" viewBox="0 0 24 24"><path d="M7 3h10a1 1 0 0 1 1 1v16a1 1 0 0 1-1 1H7a1 1 0 0 1-1-1V4a1 1 0 0 1 1-1zm1 3v11h8V6z"/></svg>
      0000 000 000
    </li>
    <li class="contacts__item">
      <svg class="contacts__icon" viewBox="0 0 24 24"><path d="M2 10l10-6 10 6v10H2zm3 1l7 5 7-5-7-4z"/></svg>
      larkfield@mail.example
    </li>
    <li class="contacts__item">
      <svg class="contacts__icon" viewBox="0 0 24 24" fill="none" stroke="var(--white)" stroke-width="1.6"><circle cx="12" cy="12" r="9"/><ellipse cx="12" cy="12" rx="4" ry="9"/><path d="M3 12h18M5 7h14M5 17h14"/></svg>
      www.larkfieldconsulting.example
    </li>
  </ul>
</section>

<section class="card card--back">
  <div class="brand">
    <span class="brand__name">Larkfield</span>
    <span class="brand__tag">CONSULTING</span>
  </div>
</section>

</body>
</html>
```